Ondas Tierra - Stationery and Presentation Materials
Biz card, letterhead, envelope, presentation folder
Bright & Fun-filled
Martin Coble
E.S.
Tel. +503.2417.8836
Cel. +503.7396.1052
U.S. +1.800.555.0147 x3061
U.S.
ondastierra.led@correoplano.com
PLEASE, DON'T POST EMAIL IN DRAFTS.
--The business is rental of large LED screens for visuals, which are made of thousands of tiny lights.
---Please give a range of crazy/abstract as well as aggressive but traditional/corporate concepts for all items in subtitle.
---The presentation folder is to digitally insert fotos later for printing. Borders are key. A CD will be included, on a plastic peg anywhere in the folder, and CD design must blend with folder graphics on the point where CD sits.
Minimal.
---try wrap-around logo
----1 "wild concept" if anyone is willing - background is very tiny, SHINING, white lights (almost pixel-looking), with the logo symbol on top.

```html
<!DOCTYPE html>
<html lang="es">
<head>
<meta charset="utf-8">
<title>Ondas Tierra – Business Card</title>
<link rel="stylesheet" href="https://fonts.googleapis.com/css2?family=Arimo:wght@400;700&display=swap">
<style>
  :root {
    --page-bg: #e9e7e4;
    --card-bg: #ffffff;
    --brand-orange: #f26a21;
    --brand-red: #e8412c;
    --brand-blue: #1f4ea3;
    --text-dark: #3a3a3a;
    --divider: #8a8fa0;
  }
  html, body {
    margin: 0;
    padding: 0;
    width: 1200px;
    height: 965px;
    overflow: hidden;
    background: var(--page-bg);
    font-family: "Arimo", Arial, sans-serif;
  }
  .business-card {
    position: absolute;
    left: 214px;
    top: 263px;
    width: 772px;
    height: 440px;
    background: var(--card-bg);
    border-radius: 26px;
    overflow: hidden;
  }
  .brand-lockup {
    position: absolute;
    left: 78px;
    top: 42px;
    height: 150px;
    display: flex;
    align-items: center;
    gap: 34px;
  }
  .brand-mark {
    width: 124px;
    height: 124px;
    background: var(--brand-orange);
  }
  .brand-name {
    font-size: 60px;
    font-weight: 700;
    color: var(--brand-red);
    line-height: 1;
  }
  .holder-name {
    position: absolute;
    left: 150px;
    top: 282px;
    margin: 0;
    font-size: 29px;
    line-height: 36px;
    font-weight: 700;
    color: var(--brand-orange);
  }
  .contact-divider {
    position: absolute;
    left: 362px;
    top: 242px;
    width: 2px;
    height: 136px;
    background: var(--divider);
  }
  .contact-list {
    position: absolute;
    left: 376px;
    top: 242px;
    margin: 0;
    padding: 0;
    list-style: none;
    font-size: 18px;
    line-height: 27px;
    color: var(--text-dark);
    white-space: nowrap;
  }
  .contact-list .label {
    color: var(--brand-blue);
    font-weight: 700;
  }
  .card-swoosh {
    position: absolute;
    left: 0;
    top: 0;
    width: 772px;
    height: 440px;
  }
</style>
</head>
<body>
  <article class="business-card">
    <svg class="card-swoosh" viewBox="0 0 772 440" aria-hidden="true">
      <defs>
        <linearGradient id="band-fill" x1="0" y1="0" x2="1" y2="0">
          <stop offset="0" stop-color="#f26a21"/>
          <stop offset="0.5" stop-color="#f7941d"/>
          <stop offset="1" stop-color="#f26a21"/>
        </linearGradient>
      </defs>
      <path d="M0 384 Q 400 425 772 400 L772 440 L0 440 Z" fill="url(#band-fill)"/>
      <path d="M0 372 Q 390 412 772 390" fill="none" stroke="#1f4ea3" stroke-width="6"/>
    </svg>

    <div class="brand-lockup">
      <div class="brand-mark"></div>
      <div class="brand-name">Ondas Tierra</div>
    </div>

    <h1 class="holder-name">Martin Coble</h1>
    <div class="contact-divider"></div>
    <ul class="contact-list">
      <li>E.S.</li>
      <li><span class="label">Tel :</span> +503.2417.8836</li>
      <li><span class="label">Cell :</span> +503.7396.1052</li>
      <li><span class="label">U.S :</span> +1.800.555.0147 x3061</li>
      <li><span class="label">Email :</span> correo pendiente</li>
    </ul>
  </article>
</body>
</html>
```